Core values in our company OPK (Residency and Relocation)

Do good:
1. Being Direct and communicative for the benefit of all parties
2. Working for the Benefit of the company, client and team members
3. Wanting to improve to create a better impact
4. Having healthy rivalry
Be ahead of curve:
1. Having the confidence to break through barriers which arise
2. Desire to grow and learn towards establishment and agreed goal
3. Getting off the sidelines and get into the game
4. Keeping the end game in mind having due regard to processes and milestones
5. Self starter and works on own initiative
6. Diligent and impactful in your field of responsibility
Truth and Honesty
2. Have the confidence and ability to speak what you really want to communicate
3. Being truthful to yourself, clients and colleagues to find the innovations that lie within
4. Seeking the truth by opening things up for discussion
5. Being Optimistic
Background Information on our Company:OPK is a professional law firm in London Docklands. We caters for both private and corporate clients ranging from highly regarded and established law firms to boutique and niche immigration practices. We also specialises in expert legal advice and prides itself on providing services that go beyond the expectations of its clients.
What we need: We need a Poster about Truth and Honesty, this is to show one of our values as a company. It will need to be vibrant and straight to the point. Colours can be orange grey white and yellow. Attached is our company logo.
Reason: To remind colleagues that this is one of our main values and it is instilled in our company.
Things we would like:
1. To create a point of focus
2. Use shapes to create visual interest
3. Use creative illustrations
4. Take the viewer’s focus on a journey with clever perspective
Industry/Entity Type
Legal
Requirements
Must have
- a globe (Picture)
- Do good:
- 1. Being Direct and communicative for the benefit of all parties
- 2. Working for the Benefit of the company, client and team members
- 3. Wanting to improve to create a better impact
- 4. Having healthy rivalry
- Be ahead of curve:
- 1. Having the confidence to break through barriers which arise
- 2. Desire to grow and learn towards establishment and agreed goal
- 3. Getting off the sidelines and get into the game
- 4. Keeping the end game in mind having due regard to processes and milestones
- 5. Self starter and works on own initiative
- 6. Diligent and impactful in your field of responsibility
- Truth and Honesty
- 2. Have the confidence and ability to speak what you really want to communicate
- 3. Being truthful to yourself, clients and colleagues to find the innovations that lie within
- 4. Seeking the truth by opening things up for discussion
- 5. Being Optimistic

```html
<!DOCTYPE html>
<html lang="en">
<head>
<meta charset="utf-8">
<title>OPK Core Values</title>
<link rel="stylesheet" href="https://fonts.googleapis.com/css2?family=Roboto+Condensed:wght@400;700&family=Libre+Baskerville&display=swap">
<style>
  :root {
    --cream: #fdf1c9;
    --cream-light: #fff8e2;
    --orange: #f7931e;
    --yellow: #fbc316;
    --charcoal: #3b3935;
    --ink: #1d1d1b;
    --space-deep: #120f33;
    --space-violet: #3d2a78;
  }
  * { margin: 0; padding: 0; box-sizing: border-box; }
  html, body { width: 848px; height: 1200px; overflow: hidden; }
  body { font-family: "Roboto Condensed", "Arial Narrow", sans-serif; color: var(--ink); }
  .poster {
    position: relative; width: 848px; height: 1200px;
    display: flex;
  }
  .values-panel {
    position: relative; width: 500px; height: 100%;
    background: radial-gradient(ellipse at 40% 20%, var(--cream-light), var(--cream) 70%);
  }
  .space-scene {
    width: 348px; height: 100%;
    background:
      radial-gradient(circle at 55% 18%, rgba(230,210,170,.55) 0 12%, transparent 13%),
      radial-gradient(circle at 50% 52%, rgba(210,200,240,.45) 0 16%, transparent 22%),
      radial-gradient(circle at 48% 88%, rgba(170,120,220,.6) 0 24%, transparent 26%),
      linear-gradient(180deg, var(--space-deep), var(--space-violet) 45%, var(--space-deep));
  }
  .brand {
    position: absolute; left: 0; width: 500px; top: 58px; text-align: center;
  }
  .brand-name {
    font-weight: 700; font-size: 104px; line-height: 1; letter-spacing: 2px;
    color: var(--charcoal);
  }
  .brand-tagline {
    margin-top: 14px;
    font-family: "Libre Baskerville", Georgia, serif; font-size: 19px;
    color: var(--charcoal);
  }
  .value {
    position: absolute; left: 0; width: 500px;
  }
  .value-title {
    position: absolute; left: 69px; top: 0;
    height: 47px; padding: 0 11px; border-radius: 9px;
    font-size: 39px; line-height: 47px; font-weight: 400; color: #fff;
    background: var(--accent);
  }
  .value-title::after {
    content: ""; position: absolute; left: 20px; top: 46px;
    border-left: 8px solid transparent; border-right: 8px solid transparent;
    border-top: 12px solid var(--accent);
  }
  .value-list {
    position: absolute; left: 79px; width: 415px; list-style: none;
  }
  .value-list::before {
    content: ""; position: absolute; left: -20px; top: 12px; bottom: 20px;
    width: 3px; background: var(--accent);
  }
  .value-list li {
    position: relative; font-size: 19.5px; line-height: 24px; margin-bottom: 8px;
  }
  .value-list li::before {
    content: ""; position: absolute; left: -26px; top: 5px;
    width: 14px; height: 14px; background: var(--accent);
  }
  .value--good { --accent: var(--orange); top: 238px; }
  .value--ahead { --accent: var(--yellow); top: 502px; }
  .value--truth { --accent: var(--charcoal); top: 852px; }
  .value--good .value-list { top: 64px; }
  .value--ahead .value-list { top: 61px; }
  .value--truth .value-list { top: 61px; }
</style>
</head>
<body>
<main class="poster">
  <section class="values-panel">
    <header class="brand">
      <div class="brand-name">OPK</div>
      <div class="brand-tagline">residency and relocation</div>
    </header>

    <article class="value value--good">
      <h2 class="value-title">DO GOOD:</h2>
      <ul class="value-list">
        <li>Being Direct and communicative for the benefit of all parties</li>
        <li>Working for the Benefit of the company, client and team members</li>
        <li>Wanting to improve to create a better impact</li>
        <li>Having healthy rivalry</li>
      </ul>
    </article>

    <article class="value value--ahead">
      <h2 class="value-title">Be a Head of Curve:</h2>
      <ul class="value-list">
        <li>Having the confidence to break through barriers which arise</li>
        <li>Desire to grow and learn towards establishment and agreed goal</li>
        <li>Getting off the sidelines and get into the game</li>
        <li>Keeping the end game in mind having due regard to processes and milestones</li>
        <li>Self starter and works on own initiative</li>
        <li>Diligent and impactful in your field of responsibility</li>
      </ul>
    </article>

    <article class="value value--truth">
      <h2 class="value-title">Truth and Honesty</h2>
      <ul class="value-list">
        <li>Having the confidence to break through barriers which arise</li>
        <li>Have the confidence and ability to speak what you really want to communicate</li>
        <li>Being truthful to yourself, clients and colleagues to find the innovations that lie within</li>
        <li>Seeking the truth by opening things up for discussion</li>
        <li>Being Optimistic</li>
      </ul>
    </article>
  </section>

  <div class="space-scene" role="img" aria-label="Purple space illustration: a ringed planet at the top, a floating astronaut in the middle, drifting asteroids, and the Earth with its moon at the bottom"></div>
</main>
</body>
</html>
```